Pages toward Inner Calm - book cover

12/18 update: Please read the entire brief. I don’t love anything that has been provided up to today. Please use the graphics and colors I’ve attached!!!! Show me your creations.

I am looking for a book cover design. It is a mental health journal. Needs to be very warm, inviting, calming. I’m very interested in new creative ideas. It will be wire-o bound and also in hard copy front and back. Use the graphic and colors I already have attached to this file. It’s called “Pages Toward Inner Calm”. Self means soul or spirit or center. The idea of integration may be a fit here in some way. If some words need to be emphasized in the design, “Self” and “QRM” would be the most important. size 6"x9". The words on the front can be smaller and more inviting then they would normally be on a fiction paperback.

Update 12/16: I am not excited about any of the submissions so far. I’m looking forward to seeing more options.

Target Market(s)

Adults 30-60. Male and female. People who like to learn. People wanting to heal. Middle and upper income.

Industry/Entity Type

Mental health. Wellness

Font styles to use
Other font styles liked:
• Whatever font is used in my logo. i don’t know the name. I also would be open to a different font if it was warm, inviting, and calm.

Colors
0094D4
00A9DD
6FCCEA
C7EBF8
E9F6FB

Requirements
Must have
• My logo colors. The words “Pages Toward Inner Calm” and “A 13-Week QRM Exploration”
Nice to have
• I’d like to see some creative ideas. More abstract than realistic.
Should not have
• No realist art or photos.

```html
<!DOCTYPE html>
<html lang="en">
<head>
<meta charset="utf-8">
<title>Pages Toward Inner Calm – Cover</title>
<link rel="stylesheet" href="https://fonts.googleapis.com/css2?family=Encode+Sans+Condensed:wght@300;400&display=swap">
<style>
  :root {
    --teal-deep: #1d5766;
    --teal-mist: #7298a0;
    --stone-light: #d0d2d4;
    --stone-mid: #939ca3;
    --paper: #ffffff;
    --type-light: #ffffff;
  }
  * { margin: 0; padding: 0; box-sizing: border-box; }
  html, body {
    width: 850px;
    height: 1200px;
    overflow: hidden;
    background: var(--paper);
  }
  .cover {
    position: relative;
    width: 850px;
    height: 1200px;
    background: var(--paper);
    font-family: "Encode Sans Condensed", "Arial Narrow", sans-serif;
    font-weight: 300;
  }
  .cover-art {
    position: absolute;
    inset: 0;
    width: 850px;
    height: 1200px;
  }
  .brand {
    position: absolute;
    top: 130px;
    right: 60px;
    display: flex;
    align-items: center;
    gap: 8px;
    color: var(--teal-deep);
    font-size: 17px;
    font-weight: 400;
    letter-spacing: 0.22em;
    text-transform: uppercase;
  }
  .brand-dot {
    width: 9px;
    height: 9px;
    border-radius: 50%;
    background: var(--teal-deep);
  }
  .title-block {
    position: absolute;
    left: 0;
    right: 0;
    top: 872px;
    text-align: center;
    color: var(--type-light);
    padding-left: 26px;
    font-weight: 300;
  }
  .title-main {
    display: block;
    font-size: 92px;
    font-weight: 300;
    line-height: 1;
    letter-spacing: -0.01em;
  }
  .title-sub {
    display: block;
    font-size: 47px;
    font-weight: 300;
    line-height: 1;
    margin-top: 2px;
  }
  .tagline {
    position: absolute;
    left: 0;
    right: 0;
    top: 1068px;
    text-align: center;
    padding-left: 26px;
    color: var(--type-light);
    font-size: 30px;
    font-weight: 300;
  }
</style>
</head>
<body>
<main class="cover">
  <svg class="cover-art" viewBox="0 0 1240 1754" preserveAspectRatio="none" aria-hidden="true">
    <defs>
      <clipPath id="lower-field">
        <polygon points="0,1030 620,775 1240,1030 1240,1754 0,1754"/>
      </clipPath>
      <clipPath id="inner-window">
        <path d="M612,500 L852,638 L852,862 L612,1022 L376,862 L376,638 Z"/>
      </clipPath>
      <radialGradient id="emblem-tone" cx="50%" cy="60%" r="55%">
        <stop offset="0%" stop-color="#1d5766"/>
        <stop offset="70%" stop-color="#1d5766" stop-opacity="0.9"/>
        <stop offset="100%" stop-color="#1d5766" stop-opacity="0.35"/>
      </radialGradient>
    </defs>

    <polygon class="lower-band" points="0,1030 620,775 1240,1030 1240,1754 0,1754" fill="var(--teal-deep)"/>

    <path class="hex-outer" d="M620,300 L1030,537 L1030,940 L620,1230 L196,945 L196,537 Z"
          fill="var(--teal-deep)" stroke="var(--teal-deep)" stroke-width="40" stroke-linejoin="round"/>
    <path class="hex-outer-lower" clip-path="url(#lower-field)"
          d="M620,300 L1030,537 L1030,940 L620,1230 L196,945 L196,537 Z"
          fill="var(--teal-mist)" stroke="var(--teal-mist)" stroke-width="40" stroke-linejoin="round"/>

    <path class="hex-frame" d="M612,445 L900,612 L900,888 L612,1076 L327,888 L327,612 Z"
          fill="var(--paper)" stroke="var(--paper)" stroke-width="36" stroke-linejoin="round"/>
    <path class="hex-inner" d="M612,480 L868,628 L868,872 L612,1042 L360,872 L360,628 Z"
          fill="var(--stone-light)" stroke="var(--stone-light)" stroke-width="34" stroke-linejoin="round"/>
    <path class="hex-inner-lower" clip-path="url(#lower-field)"
          d="M612,480 L868,628 L868,872 L612,1042 L360,872 L360,628 Z"
          fill="var(--stone-mid)" stroke="var(--stone-mid)" stroke-width="34" stroke-linejoin="round"/>

    <g clip-path="url(#inner-window)">
      <rect class="emblem" x="400" y="540" width="425" height="455" rx="140"
            fill="url(#emblem-tone)" role="img"
            aria-label="Emblem of two cupped hands holding a falling water drop"/>
    </g>
  </svg>

  <div class="brand"><span class="brand-dot"></span>Larkin Wellness</div>

  <h1 class="title-block">
    <span class="title-main">Pages</span>
    <span class="title-sub">Toward Inner Calm</span>
  </h1>

  <p class="tagline">A 13-Week QRM Exploration</p>
</main>
</body>
</html>
```